Love-Drama Movie Flyer for World Sales Pitch

Dear Designers

We need for a world sales pitch a flyer for our new movie MARBLEFIN. We need a front and a back page A4.
Front: One picture we deliver for then whole page, title, some "pitch" sentences
Picture Front: https://www.fileharbor-example.net/s/qk83tnb2px71vd9/Front_Picture.jpg?dl=0
Back: Arrangement of title, 5 pictures and text we deliver (attached)

Please find in the attached examples a rough idea what we’re looking for. Should not be exactly the same.

To get an Impression of the content and style of the film, please watch the 3min teaser. This will be very important for the style of the flyer:
https://clipvault-example.net/487316920
pw: tutumarblefin

In the end we prefer a data package with the flyer made in a adobe design application for high quality print.

Thanks
Tomas Vrelnik
Producer

Target Market(s)

High profile film sales professionals

Industry/Entity Type

Film Production

Requirements
Must have
• see description
Should not have
• not too generic,
• there is the color red on the actors pullover but red is not really a color in the film. So please don't use much red
• Awards of the actor/actress are not for this movie, it's from other movies

```html
<!DOCTYPE html>
<html lang="en">
<head>
<meta charset="utf-8">
<title>MARBLEFIN – Flyer Front, Dark Theme</title>
<link rel="stylesheet" href="https://fonts.googleapis.com/css2?family=Roboto:wght@300;400;700&display=swap">
<style>
  :root {
    --page: #ffffff;
    --poster: #0b0b0c;
    --ink-strong: #c9c9c9;
    --ink-soft: #b3b3b3;
    --ink-dim: #6f6f6f;
    --accent: #d42b1e;
    --note: #8a8a8a;
  }
  * { margin: 0; padding: 0; box-sizing: border-box; }
  html, body {
    width: 1200px; height: 1000px; overflow: hidden;
    background: var(--page);
    font-family: "Roboto", "Helvetica Neue", Arial, sans-serif;
  }
  .canvas { position: relative; width: 1200px; height: 1000px; }

  .poster {
    position: absolute; left: 82px; top: 0; width: 707px; height: 1000px;
    background: var(--poster); overflow: hidden;
  }
  .giant-shadow {
    position: absolute; left: 50px; top: 0; width: 630px; height: 1000px;
    border-radius: 220px 220px 0 0;
    background: radial-gradient(ellipse at 50% 30%, #2a2a2c 0%, #1a1a1c 45%, #0d0d0e 80%);
  }
  .hero-figure {
    position: absolute; left: 104px; top: 92px; width: 236px; height: 760px;
    border-radius: 80px 80px 20px 20px;
    background: linear-gradient(180deg, #3a3a3c 0%, #2d2d30 40%, #1f2533 62%, #1b2130 92%, #2b2b2b 100%);
  }

  .tagline-vertical {
    position: absolute; left: 96px; top: 780px;
    transform: rotate(-90deg); transform-origin: left top;
    font-weight: 300; font-size: 40px; letter-spacing: 1px;
    color: var(--ink-dim); white-space: nowrap;
  }

  .credits { position: absolute; left: 385px; top: 0; width: 300px; }
  .cast-name {
    position: absolute; left: 0; white-space: nowrap;
    font-weight: 300; font-size: 23px; color: var(--ink-soft); letter-spacing: -0.3px;
  }
  .cast-name .quote { font-weight: 700; font-size: 22px; }
  .award {
    position: absolute; left: 20px;
    font-size: 21px; line-height: 20px; letter-spacing: -0.6px;
    text-transform: uppercase; color: var(--ink-strong);
  }
  .award b { font-weight: 700; }
  .award .light { font-weight: 400; }
  .award .film { display: block; font-weight: 400; color: var(--accent); }

  .director {
    position: absolute; left: 0; width: 707px; top: 875px; text-align: center;
    font-size: 13px; color: var(--ink-soft); letter-spacing: 0.3px;
  }
  .title {
    position: absolute; left: 0; width: 707px; top: 886px; text-align: center;
    font-weight: 300; font-size: 80px; line-height: 1; letter-spacing: 1px;
    color: #9a9a9a;
    background: linear-gradient(180deg, #d6d6d6, #7a7a7a);
    -webkit-background-clip: text; background-clip: text; -webkit-text-fill-color: transparent;
  }
  .release {
    position: absolute; left: 0; width: 707px; top: 964px; text-align: center;
    font-size: 12px; color: var(--ink-soft); letter-spacing: 0.3px;
  }

  .notes { position: absolute; left: 831px; top: 206px; width: 330px; color: var(--note); }
  .notes-heading { font-weight: 300; font-size: 44px; line-height: 57px; }
  .notes-body { margin-top: 22px; font-weight: 300; font-size: 20px; line-height: 28px; }
  .notes-body p + p { margin-top: 28px; }
</style>
</head>
<body>
<main class="canvas">
  <section class="poster">
    <div class="giant-shadow" role="img" aria-label="Large dark silhouette of a hooded figure looming in the background"></div>
    <div class="hero-figure" role="img" aria-label="Full-length photo of a young man in a dark hoodie and jeans, hands in pockets"></div>

    <div class="tagline-vertical">THIS IS DAVID</div>

    <div class="credits">
      <div class="cast-name" style="top:134px"><span class="quote">“</span> JONAS REITER <span class="quote">”</span></div>
      <div class="award" style="top:187px"><b>Alpine Screen Award<br>2015</b> <span class="light">Best Actor</span><span class="film">The Ring Road</span></div>
      <div class="award" style="top:267px"><b>Continental Rising<br>Star 2015</b></div>
      <div class="award" style="top:329px"><b>Recurring<br>appearance in the<br>award winning<br>US series</b><span class="film">Borderline</span></div>

      <div class="cast-name" style="top:480px"><span class="quote">“</span> LENA MARIT KOHL <span class="quote">”</span></div>
      <div class="award" style="top:535px"><b>Orbit Award<br>Nominee 2016</b><br><span class="light">Best Actress</span><span class="film">Notes on a Girl</span></div>
      <div class="award" style="top:636px"><b>Southern Film<br>Prize 2015</b><br><span class="light">Best Young Actress</span><span class="film">Notes on a Girl</span></div>
      <div class="award" style="top:737px"><b>Fresh Screen Award<br>2012</b><br><span class="light">Best Actress</span><span class="film">Margarete</span></div>
    </div>

    <div class="director">A FILM BY ANSELM BRUGGER</div>
    <h1 class="title">MARBLEFIN</h1>
    <div class="release">COMING FALL 2016</div>
  </section>

  <aside class="notes">
    <h2 class="notes-heading">Sample 01<br>Front<br>(Dark theme)</h2>
    <div class="notes-body">
      <p>The shade behind<br>represent the marblefin,<br>or the monster/giant/darker<br>side of his inner-self.</p>
      <p>I think this is what the<br>movie about..<br>David vs Marblefin (fighting his<br>evil side)<br>I’ve seen the teaser, but i can’t<br>understand what they’re<br>saying. i’m sorry if i got it<br>wrong.</p>
    </div>
  </aside>
</main>
</body>
</html>
```